Ward Compass Business Card Design*

We need a business card design for our company Ward Compass. Our company is specialized in providing online consulting services regarding medical institutions, hospitals and doctors. We work with patients worldwide looking to choose between healthcare providers. We have a website you may use as a reference, where we list doctors and clinics worldwide. So we target Medical providers as well as patients worldwide.
Target Market(s)
Medical Providers and patients around the world
Industry/Entity Type
Medical
Contact Information for Business Card
Salma Derkaoui
CEO
+90 612 348 2071
info@wardcompass-example.com
www.wardcompass-example.com
14 Annakhil 3 H.R.B. Rabat, Morocco
Requirements
Must have
- Company logo/name on one full side, personal info and smaller logo and company name on the other side.
Nice to have
- Smart and elegant design

```html
<!DOCTYPE html>
<html lang="en">
<head>
<meta charset="utf-8">
<title>Ward Compass – Business Card</title>
<link rel="stylesheet" href="https://fonts.googleapis.com/css2?family=Montserrat:wght@300;400;600;700&family=Open+Sans:wght@400;600&display=swap">
<style>
  :root {
    --backdrop: #1c1c1e;
    --navy: #0d3068;
    --navy-deep: #0a2656;
    --paper: #f7f7f8;
    --grey-text: #8a8c92;
    --ink: #1e2330;
    --white: #ffffff;
  }
  * { box-sizing: border-box; margin: 0; padding: 0; }
  html, body {
    width: 1200px; height: 900px; overflow: hidden;
    background: var(--backdrop);
  }
  .canvas { position: relative; width: 1200px; height: 900px; }

  .card {
    position: absolute;
    width: 560px; height: 320px;
    border-radius: 3px;
    box-shadow: 0 18px 40px rgba(0,0,0,.55);
    overflow: hidden;
  }

  /* Front side */
  .card--front {
    left: 80px; top: 120px;
    background: linear-gradient(160deg, var(--navy) 0%, var(--navy-deep) 100%);
    color: var(--white);
  }
  .card--front .brand {
    position: absolute; left: 0; right: 0; top: 118px;
    display: flex; align-items: center; justify-content: center; gap: 18px;
  }
  .brand__dot {
    width: 58px; height: 58px; border-radius: 50%;
    border: 9px solid var(--white);
  }
  .brand__name {
    font-family: "Montserrat", sans-serif;
    font-weight: 600; font-size: 34px; letter-spacing: 2px;
    text-transform: uppercase;
  }
  .card--front .website {
    position: absolute; left: 0; right: 0; bottom: 38px;
    text-align: center;
    font-family: "Montserrat", sans-serif;
    font-weight: 700; font-size: 13px; letter-spacing: 3px;
  }

  /* Back side */
  .card--back {
    left: 560px; top: 460px;
    background: var(--paper);
    color: var(--ink);
  }
  .card--back .brand {
    position: absolute; left: 0; right: 0; top: 86px;
    display: flex; align-items: center; justify-content: center; gap: 14px;
    color: var(--navy);
  }
  .card--back .brand__dot {
    width: 44px; height: 44px; border-width: 7px; border-color: var(--navy);
  }
  .card--back .brand__name { font-size: 26px; }

  .person {
    position: absolute; right: 300px; top: 218px;
    text-align: right;
    font-family: "Montserrat", sans-serif;
  }
  .person__name { font-size: 15px; color: var(--navy); letter-spacing: .5px; }
  .person__first { font-weight: 700; }
  .person__last { font-weight: 300; color: var(--grey-text); }
  .person__role { font-size: 10px; font-weight: 600; color: var(--ink); margin-top: 3px; letter-spacing: 1px; }

  .divider {
    position: absolute; left: 280px; top: 198px;
    width: 2px; height: 74px;
    background: linear-gradient(180deg, rgba(13,48,104,0) 0%, var(--navy) 50%, rgba(13,48,104,0) 100%);
  }

  .contact {
    position: absolute; left: 302px; top: 210px;
    list-style: none;
    font-family: "Open Sans", sans-serif; font-size: 12.5px; color: var(--ink);
  }
  .contact li { display: flex; align-items: center; gap: 9px; height: 24px; }
  .contact svg { width: 14px; height: 14px; fill: var(--navy); flex: none; }
</style>
</head>
<body>
<main class="canvas">

  <section class="card card--front" aria-label="Card front">
    <div class="brand">
      <span class="brand__dot" aria-hidden="true"></span>
      <span class="brand__name">Ward Compass</span>
    </div>
    <p class="website">www.wardcompass-example.com</p>
  </section>

  <section class="card card--back" aria-label="Card back">
    <div class="brand">
      <span class="brand__dot" aria-hidden="true"></span>
      <span class="brand__name">Ward Compass</span>
    </div>

    <div class="person">
      <p class="person__name"><span class="person__first">SALMA</span> <span class="person__last">DERKAOUI</span></p>
      <p class="person__role">CEO</p>
    </div>

    <div class="divider" aria-hidden="true"></div>

    <ul class="contact">
      <li>
        <svg viewBox="0 0 24 24" aria-hidden="true"><path d="M6.6 10.8a15.1 15.1 0 0 0 6.6 6.6l2.2-2.2c.3-.3.7-.4 1-.2 1.1.4 2.3.6 3.6.6.6 0 1 .4 1 1V20c0 .6-.4 1-1 1A17 17 0 0 1 3 4c0-.6.4-1 1-1h3.5c.6 0 1 .4 1 1 0 1.3.2 2.5.6 3.6.1.3 0 .7-.2 1z"/></svg>
        <span>+90 612 348 2071</span>
      </li>
      <li>
        <svg viewBox="0 0 24 24" aria-hidden="true"><path d="M2 5h20v14H2z M2 5l10 8 10-8" fill="none" stroke="#0d3068" stroke-width="2"/></svg>
        <span>info@wardcompass-example.com</span>
      </li>
    </ul>
  </section>

</main>
</body>
</html>
```